Full color cover for Chamber's Membership Menu

I need a cover, 8 1/2" x 11" for our Chamber of Commerce Membership Menu. Is should have our logo and the words, Membership Menu on it. That's all that is necessary but it can include one or more of the other photos (maybe a college?) that I added, though they are not required. Our logo colors should be used: 37-170-226, 58-181-74, 40-56-144, 247-148-29, 189-190-192.

Target Market(s)

Business owners and managers

Industry/Entity Type

Business Development

Font styles to use
Serif

Colors
0054AA
0677BA
7BADD7
CADEEF
E8F1F8
00AB8E
00BBA5
67D7C9
C6EFE9
E9F9F6
F0912C
F2A743
F7CA91
FBE8D2
FDF5EE

Requirements
Must have
• Our logo and the words Membership Menu
Nice to have
• An attractive business-like feel. It can be very simple.

```html
<!DOCTYPE html>
<html lang="en">
<head>
<meta charset="utf-8">
<title>Membership Menu Cover</title>
<link href="https://fonts.googleapis.com/css2?family=Pinyon+Script&family=Roboto+Condensed:wght@700&display=swap" rel="stylesheet">
<style>
  :root {
    --teal-deep: #3f9e9f;
    --blue-deep: #17507f;
    --teal-light: #67D7C9;
    --teal-band: #10b3a0;
    --teal-strip: #4cc0b6;
    --orange: #F0912C;
    --peach: #F7CA91;
    --navy: #283890;
    --dot: #1f9aa0;
  }
  html, body {
    margin: 0;
    padding: 0;
    overflow: hidden;
    background: #ffffff;
  }
  .cover {
    position: relative;
    width: 927px;
    height: 1200px;
    overflow: hidden;
  }
  .cover-art {
    position: absolute;
    inset: 0;
    display: block;
  }
  .cover-title {
    position: absolute;
    left: 0;
    right: 0;
    top: 720px;
    margin: 0;
    text-align: center;
    font-family: "Pinyon Script", cursive;
    font-weight: 400;
    font-size: 78px;
    color: var(--peach);
    letter-spacing: 1px;
  }
  .chamber-mark {
    position: absolute;
    left: 530px;
    top: 990px;
    width: 340px;
    text-align: center;
    font-family: "Roboto Condensed", sans-serif;
    font-weight: 700;
    color: var(--navy);
  }
  .chamber-mark__dot {
    width: 84px;
    height: 84px;
    margin: 0 auto 18px;
    border-radius: 50%;
    background: var(--navy);
  }
  .chamber-mark__name {
    display: block;
    font-size: 34px;
    line-height: 1;
    letter-spacing: 0.5px;
  }
  .chamber-mark__tagline {
    display: block;
    margin-top: 4px;
    font-size: 17px;
    letter-spacing: 4px;
  }
</style>
</head>
<body>
<main class="cover">
  <svg class="cover-art" viewBox="0 0 927 1200" width="927" height="1200" xmlns="http://www.w3.org/2000/svg">
    <defs>
      <linearGradient id="photoTone" x1="0" y1="0" x2="1" y2="1">
        <stop offset="0" stop-color="#b9e0c9"/>
        <stop offset="0.45" stop-color="#8fb6a6"/>
        <stop offset="1" stop-color="#6e6a6c"/>
      </linearGradient>
      <linearGradient id="bodyTone" x1="0" y1="0" x2="0" y2="1">
        <stop offset="0" stop-color="var(--teal-deep)"/>
        <stop offset="1" stop-color="var(--blue-deep)"/>
      </linearGradient>
    </defs>

    <rect class="hero-photo" role="img" aria-label="Photo of a group of business members cutting a blue ribbon at a local restaurant opening" x="0" y="0" width="927" height="660" fill="url(#photoTone)"/>

    <path class="wave-strip" d="M0,505 C110,575 210,615 330,612 C430,608 470,585 540,565 C690,525 820,520 927,545 L927,1200 L0,1200 Z" fill="var(--teal-strip)"/>
    <path class="wave-body" d="M0,560 C160,640 330,660 480,625 C650,585 800,570 927,590 L927,1200 L0,1200 Z" fill="url(#bodyTone)"/>

    <path class="swoosh-left" d="M0,485 C100,545 220,578 350,543 L352,548 C220,590 100,565 0,520 Z" fill="var(--orange)"/>
    <path class="swoosh-right" d="M450,585 C600,505 780,488 927,515 L927,565 C780,525 620,530 450,585 Z" fill="var(--orange)"/>

    <g class="dot-grid" fill="var(--dot)" opacity="0.45">
      <circle cx="705" cy="545" r="22"/><circle cx="755" cy="545" r="22"/><circle cx="805" cy="545" r="22"/><circle cx="855" cy="545" r="22"/><circle cx="905" cy="545" r="22"/>
      <circle cx="705" cy="595" r="22"/><circle cx="755" cy="595" r="22"/><circle cx="805" cy="595" r="22"/><circle cx="855" cy="595" r="22"/><circle cx="905" cy="595" r="22"/>
      <circle cx="705" cy="622" r="22"/><circle cx="755" cy="622" r="22"/><circle cx="805" cy="622" r="22"/><circle cx="855" cy="622" r="22"/><circle cx="905" cy="622" r="22"/>
    </g>

    <path class="corner-band" d="M315,1200 C400,990 550,915 750,880 C840,864 895,840 927,818 L927,1200 Z" fill="var(--teal-band)"/>
    <path class="corner-panel" d="M345,1200 C430,1010 575,945 770,915 C855,902 900,880 927,862 L927,1200 Z" fill="var(--teal-light)"/>

    <g class="dot-row" fill="var(--dot)">
      <circle cx="68" cy="1150" r="22"/>
      <circle cx="117" cy="1150" r="22"/>
      <circle cx="166" cy="1150" r="22"/>
      <circle cx="215" cy="1150" r="22"/>
      <circle cx="264" cy="1150" r="22"/>
    </g>
  </svg>

  <h1 class="cover-title">Membership Menu</h1>

  <div class="chamber-mark">
    <div class="chamber-mark__dot"></div>
    <span class="chamber-mark__name">HARBORVIEW CHAMBER</span>
    <span class="chamber-mark__tagline">OF COMMERCE &amp; TOURISM</span>
  </div>
</main>
</body>
</html>
```